Offshore Energy Projects Management Consultancy needs a business card design

Logo available. We provide teams to deliver engineering consultancy, project management and delivery teams mainly in the offshore renewables sector. The company is all about bringing the right people to a project to deliver the scope.

The business card will be used for all staff.

The business card should be quite simple, vibrant and uncluttered but convey experience, enthusiasm and integration.

Target Market(s)

Energy Project Developers and Tier 1 construction companies

Contact Information for Business Card

Logo should be on the back of the card. I'm happy for the designer to play with the colour of the logo and background colour.

Front of the card should convey all the must have information in a clear and professional manner but without being overly traditional.

Colors

Designer to choose colors to be used in the design.

Requirements
Must have
• Land Line Tel Number, Mobile Tel Number, Email, business address, web address.

```html
<!DOCTYPE html>
<html lang="en">
<head>
<meta charset="utf-8">
<title>Tidewater Delivery Group – Business Card</title>
<link rel="stylesheet" href="https://fonts.googleapis.com/css2?family=Ubuntu:wght@400;500&display=swap">
<style>
  :root {
    --page-bg: #e6e2dd;
    --blue-deep: #3b6a99;
    --blue-mid: #5384b3;
    --blue-light: #7ea5c9;
    --frost: #dcd6ce;
    --frost-light: #ebe7e1;
    --curve-edge: #4d4944;
    --text-light: #f3f6fa;
    --text-soft: #e3ebf3;
    --brand-grey: #4a4d55;
    --brand-blue: #2f7fc0;
  }
  html, body {
    margin: 0;
    width: 1200px;
    height: 1054px;
    overflow: hidden;
    background: var(--page-bg);
  }
  .card {
    position: absolute;
    left: 100px;
    top: 225px;
    width: 1000px;
    height: 604px;
    box-shadow: 0 18px 40px rgba(40, 40, 50, 0.18);
  }
  .card text {
    font-family: "Ubuntu", sans-serif;
  }
  .holder-name { font-size: 37px; font-weight: 500; fill: var(--text-light); }
  .holder-role { font-size: 24px; font-weight: 400; fill: var(--text-soft); }
  .contact-line { font-size: 23px; font-weight: 400; fill: var(--text-light); }
  .contact-icon { fill: var(--text-soft); }
  .globe-icon { fill: none; stroke: var(--text-soft); stroke-width: 1.6; }
  .brand-name { font-weight: 500; fill: var(--brand-grey); }
  .brand-name-main { font-size: 36px; }
  .brand-name-sub { font-size: 20px; }
</style>
</head>
<body>
<svg class="card" viewBox="0 0 1000 604" width="1000" height="604" aria-label="Business card for Tidewater Delivery Group">
  <defs>
    <linearGradient id="blueField" x1="0" y1="0" x2="1" y2="1">
      <stop offset="0" stop-color="#7ea5c9"/>
      <stop offset="0.45" stop-color="#5384b3"/>
      <stop offset="1" stop-color="#3b6a99"/>
    </linearGradient>
    <linearGradient id="frostField" x1="0" y1="0" x2="1" y2="1">
      <stop offset="0" stop-color="#ebe7e1"/>
      <stop offset="1" stop-color="#dcd6ce"/>
    </linearGradient>
  </defs>

  <rect class="brand-side" x="0" y="0" width="1000" height="604" fill="url(#frostField)"/>

  <path class="curve-edge" d="M0 0 H640 Q500 300 595 604 H0 Z" fill="var(--curve-edge)"/>
  <path class="info-panel" d="M0 0 H628 Q488 300 583 604 H0 Z" fill="url(#blueField)"/>

  <path class="facet" d="M250 0 H628 Q560 150 548 300 L380 390 Z" fill="#ffffff" opacity="0.10"/>
  <path class="facet" d="M0 430 L380 390 L556 390 Q560 500 583 604 H0 Z" fill="#1f4a78" opacity="0.18"/>

  <text class="holder-name" x="70" y="162">Mara Lindqvist</text>
  <text class="holder-role" x="70" y="198">Managing Director</text>

  <text class="contact-line" x="70" y="292">88 Harbour Row, Port Ellis,</text>
  <text class="contact-line" x="70" y="324">Seaford, US 204815</text>
  <line class="address-rule" x1="70" y1="337" x2="320" y2="337" stroke="var(--text-soft)" stroke-width="2"/>

  <g class="contact-icon" transform="translate(72 356)">
    <path d="M2 6 Q11 -1 20 6 L18 10 L14 8 L8 8 L4 10 Z"/>
    <rect x="5" y="10" width="12" height="8" rx="2"/>
  </g>
  <text class="contact-line" x="117" y="374">041 555 0182</text>

  <g class="contact-icon" transform="translate(72 390)">
    <path d="M2 6 Q11 -1 20 6 L18 10 L14 8 L8 8 L4 10 Z"/>
    <rect x="5" y="10" width="12" height="8" rx="2"/>
  </g>
  <text class="contact-line" x="117" y="408">041 555 0247</text>

  <g class="contact-icon" transform="translate(72 426)">
    <rect x="0" y="0" width="21" height="14" rx="1"/>
    <path d="M1 1 L10.5 8 L20 1" fill="none" stroke="var(--blue-mid)" stroke-width="1.6"/>
  </g>
  <text class="contact-line" x="117" y="442">mara@tidewaterdelivery.com</text>

  <g class="globe-icon" transform="translate(82 468)">
    <circle cx="0" cy="0" r="9"/>
    <ellipse cx="0" cy="0" rx="4" ry="9"/>
    <line x1="-9" y1="0" x2="9" y2="0"/>
  </g>
  <text class="contact-line" x="117" y="476">www.tidewaterdelivery.com</text>

  <circle class="brand-dot" cx="760" cy="300" r="12" fill="var(--brand-blue)"/>
  <text class="brand-name brand-name-main" transform="translate(836 533) rotate(-90)" textLength="462" lengthAdjust="spacingAndGlyphs">TIDEWATER DELIVERY</text>
  <text class="brand-name brand-name-sub" transform="translate(864 452) rotate(-90)" textLength="300" lengthAdjust="spacing">GROUP</text>
</svg>
</body>
</html>
```